Kestrel Vitality a Centre Pty Ltd

Business card is to promote and represent our new business. It's situated in
47 Fenwick Road
Brookvale 2100 Sydney
Our clinic is all about getting people back to great health giving them back their lifestyle in half the usual time it takes to get results elsewhere , we do this through innovative therapies with latest state of the art equipment ,skills ,knowledge and experience.
We give them back their pain free healthy lifestyle with lots of energy to love life and perform their best Quickly and effectively .
The final design should communicate
Trust , confidence, results .
Updates

Reason: Waiting for some designers to submit work Thanks

Target Market(s)

High end clients that take their health and results seriously ,
High end athletes , as well as general people that want to see results with different
Treatment Methods and approach

Industry/Entity Type

Clinic

Contact Information for Business Card

Kestrel Vitality Centre Pty Ltd
47 Fenwick Road Brookvale 2100 Sydney
Website www.kestrelvitalitycentre.com.au

Font styles to use
Other font styles liked:
• Gothic font medium

Requirements
Must have
• A designe that makes people look twice with a wow factor , a designe that isn't like all the rest .
• Must have the logo in the colours Iv provided in my files
• Must communicate Trust, confidence , results
Nice to have
• 1) The logo raised up or
• 2) Maybe a pop up logo on the card ?
• Or let's be creative and have two cards one on top of the other so the two cards slide .... The front will have the kestrel logo with the address details etc
• The other card with have
• eg your next app .......................................repeating all way down the card
Should not have
• Basic plain looking card that everyone else has

```html
<!DOCTYPE html>
<html lang="en">
<head>
<meta charset="utf-8">
<title>Kestrel Vitality Centre – Business Card</title>
<link rel="stylesheet" href="https://fonts.googleapis.com/css2?family=Exo+2:wght@400;500;600;700&display=swap">
<style>
  :root {
    --backdrop: #e4e5e7;
    --card: #ffffff;
    --brand-navy: #2d3c8e;
    --brand-green: #4f9e36;
    --brand-green-dark: #3b8430;
    --name-bronze: #8c5a2a;
    --ink: #3a3a3a;
    --ink-soft: #555;
    --rule: #6bb04a;
  }
  * { box-sizing: border-box; margin: 0; padding: 0; }
  html, body {
    width: 1052px; height: 1200px; overflow: hidden;
    background: var(--backdrop);
    font-family: "Exo 2", sans-serif;
  }
  .canvas { position: relative; width: 1052px; height: 1200px; }
  .card {
    position: absolute; left: 76px; width: 900px; height: 514px;
    background: var(--card);
    box-shadow: 0 8px 24px rgba(0,0,0,0.12);
    overflow: hidden;
  }
  .card--front { top: 56px; }
  .card--back { top: 630px; }

  .wordmark {
    display: flex; align-items: center; gap: 14px;
    color: var(--brand-navy); font-weight: 600;
  }
  .wordmark__dot {
    width: 22px; height: 22px; border-radius: 50%;
    background: var(--brand-green);
  }
  .card--front .wordmark {
    position: absolute; left: 50%; top: 50%;
    transform: translate(-50%, -50%);
    font-size: 44px; white-space: nowrap;
  }
  .card--back .wordmark {
    position: absolute; left: 520px; top: 200px;
    font-size: 30px; white-space: nowrap;
  }

  .identity { position: absolute; left: 60px; top: 96px; }
  .identity__name {
    color: var(--name-bronze); font-size: 34px; font-weight: 600;
    letter-spacing: 1px; text-transform: uppercase;
  }
  .identity__title {
    color: var(--ink); font-size: 20px; font-weight: 600;
    letter-spacing: 1.5px; text-transform: uppercase; margin-top: 2px;
  }
  .identity__rule {
    position: absolute; left: 0; top: 196px; width: 380px; height: 2px;
    background: linear-gradient(90deg, var(--rule), rgba(107,176,74,0.15));
  }

  .contact-rail {
    position: absolute; left: 0; top: 306px; width: 84px; height: 208px;
    background: var(--brand-green);
  }
  .contact-rail svg { position: absolute; left: 30px; width: 24px; height: 24px; fill: #fff; }
  .contact-tab {
    position: absolute; left: 84px; width: 10px; height: 16px;
    background: var(--brand-green);
    clip-path: polygon(0 0, 100% 50%, 0 100%);
  }
  .contact-list {
    position: absolute; left: 110px; top: 308px;
    list-style: none; color: var(--ink-soft); font-size: 17px; font-weight: 500;
  }
  .contact-list li { height: 34px; line-height: 34px; }
  .contact-list li.contact-list__address { line-height: 22px; margin-top: 10px; }
</style>
</head>
<body>
<main class="canvas">

  <section class="card card--front" aria-label="Card front">
    <div class="wordmark"><span class="wordmark__dot"></span>Kestrel Vitality Centre</div>
  </section>

  <section class="card card--back" aria-label="Card back">
    <div class="identity">
      <p class="identity__name">Liam Hartley</p>
      <p class="identity__title">General Manager</p>
    </div>
    <div class="identity__rule" style="top:196px;left:0;width:420px;"></div>

    <div class="wordmark"><span class="wordmark__dot"></span>Kestrel Vitality Centre</div>

    <div class="contact-rail">
      <svg style="top:14px" viewBox="0 0 24 24" aria-hidden="true"><path d="M6.6 10.8a15 15 0 0 0 6.6 6.6l2.2-2.2a1 1 0 0 1 1-.25 11.4 11.4 0 0 0 3.6.57 1 1 0 0 1 1 1V20a1 1 0 0 1-1 1A17 17 0 0 1 3 4a1 1 0 0 1 1-1h3.5a1 1 0 0 1 1 1c0 1.25.2 2.45.57 3.57a1 1 0 0 1-.25 1z"/></svg>
      <svg style="top:48px" viewBox="0 0 24 24" aria-hidden="true"><path d="M3 5h18v14H3z M4 6l8 6 8-6" stroke="#4f9e36" stroke-width="1.6"/></svg>
      <svg style="top:82px" viewBox="0 0 24 24" aria-hidden="true"><circle cx="12" cy="12" r="9" fill="none" stroke="#fff" stroke-width="1.8"/><path d="M3 12h18M12 3c3 3 3 15 0 18M12 3c-3 3-3 15 0 18" fill="none" stroke="#fff" stroke-width="1.4"/></svg>
      <svg style="top:136px" viewBox="0 0 24 24" aria-hidden="true"><path d="M12 2a7 7 0 0 0-7 7c0 5 7 13 7 13s7-8 7-13a7 7 0 0 0-7-7zm0 9.5A2.5 2.5 0 1 1 12 6.5a2.5 2.5 0 0 1 0 5z"/></svg>
    </div>
    <span class="contact-tab" style="top:315px"></span>
    <span class="contact-tab" style="top:349px"></span>
    <span class="contact-tab" style="top:383px"></span>
    <span class="contact-tab" style="top:440px"></span>

    <ul class="contact-list">
      <li>02 9905 4127</li>
      <li>hello@kestrelvitality.com.au</li>
      <li>www.kestrelvitalitycentre.com.au</li>
      <li class="contact-list__address">47 Fenwick Road,<br>Brookvale 2100 Sydney</li>
    </ul>
  </section>

</main>
</body>
</html>
```